Botanical catalogue inspired by midcentury pacific travel brochure

Hi! We are a business specializing in the sale of botanical teas from the south pacific and southeast Asia. We are looking for a catalogue design that is reminiscent of a 1950s travel agency brochure with two separate sections. The first should 'feel' like Hawaii/Fiji/Tahiti, and the other should feel like Thailand/Indonesia/Malaysia. We would like to highlight one to three products per page.

Target Market(s)

B2B

Industry/Entity Type

Botanicals, teas, kava

Requirements
Must have
• A clear midcentury inspiration and Pacific motifs
Should not have
• Contemporary fonts or imagery

```html
<!DOCTYPE html>
<html lang="en">
<head>
<meta charset="utf-8">
<title>Lagoon Leaf Tea – Catalogue</title>
<link rel="stylesheet" href="https://fonts.googleapis.com/css2?family=Parisienne&family=Old+Standard+TT:ital,wght@0,400;0,700;1,400&display=swap">
<style>
  :root {
    --page: #f1f1f1;
    --page-mid: #e3e3e3;
    --sepia-light: #cfc6b3;
    --sepia-dark: #6e6553;
    --band: #bdbdbd;
    --band-light: #d8d8d8;
    --green: #4f6b57;
    --ink: #3a3a3a;
    --text: #666666;
    --white: #ffffff;
  }
  * { box-sizing: border-box; margin: 0; padding: 0; }
  html, body { width: 849px; height: 1200px; overflow: hidden; background: var(--page); }
  .catalogue-page {
    position: relative; width: 849px; height: 1200px; overflow: hidden;
    background: linear-gradient(180deg, var(--page) 0%, var(--page-mid) 55%, var(--page) 100%);
    font-family: "Old Standard TT", Georgia, serif; color: var(--text);
  }
  .hero-scene {
    position: absolute; left: 0; top: 0; width: 849px; height: 250px;
    background: linear-gradient(180deg, var(--sepia-dark) 0%, var(--sepia-light) 48%, #e4e0d7 75%, rgba(241,241,241,0) 100%);
  }
  .sailboat-backdrop {
    position: absolute; right: 0; top: 230px; width: 300px; height: 620px;
    background: radial-gradient(ellipse at 60% 40%, rgba(180,180,180,.35), rgba(241,241,241,0) 70%);
  }
  .contact-block { position: absolute; left: 28px; top: 22px; display: flex; align-items: center; gap: 14px; }
  .logo-spot {
    width: 68px; height: 68px; border-radius: 50%; background: var(--green);
    color: var(--white); display: flex; align-items: center; justify-content: center;
    font-size: 15px;
  }
  .contact-lines { color: var(--white); font-size: 14px; line-height: 17px; }
  .brand-mark {
    position: absolute; left: 0; top: 196px; width: 849px;
    display: flex; align-items: center; justify-content: center; gap: 14px;
  }
  .brand-dot { width: 18px; height: 18px; border-radius: 50%; background: var(--green); }
  .brand-name {
    font-size: 30px; font-weight: 400; color: var(--green);
    letter-spacing: 4px; text-transform: uppercase; line-height: 1;
  }
  .product { position: absolute; left: 0; width: 849px; }
  .product-band {
    position: absolute; left: 0; width: 849px; height: 4px; top: 40px;
    background: linear-gradient(90deg, var(--band), var(--band-light) 70%, rgba(216,216,216,0));
  }
  .band-ornament {
    position: absolute; left: 72px; top: 26px; width: 46px; height: 32px;
    background: var(--band); border-radius: 50%;
  }
  .product-title {
    position: absolute; left: 290px; top: 0; font-family: "Parisienne", cursive;
    font-size: 38px; color: var(--ink); font-weight: 400;
  }
  .product-photo {
    position: absolute; left: 72px; top: 82px; width: 198px; height: 168px;
    border: 4px solid var(--white); box-shadow: 0 1px 4px rgba(0,0,0,.25);
  }
  .photo-vanilla { background: radial-gradient(circle at 50% 50%, #3a2c20, #5c4632 55%, #f4f1ec 80%); }
  .photo-mamaki { background: radial-gradient(circle at 50% 50%, #7a6243, #4a3a28 50%, #c9a46e 70%, #3b2c1f 100%); }
  .photo-black { background: linear-gradient(160deg, #2a2018, #4d3b2a 50%, #2b2119); }
  .product-copy {
    position: absolute; left: 300px; top: 82px; width: 482px;
    font-size: 14.6px; line-height: 18px; text-align: justify;
  }
  .drop-cap {
    float: left; font-size: 52px; line-height: 40px; color: var(--ink);
    margin: 2px 6px 0 0;
  }
  .footer-ornament {
    position: absolute; left: 72px; top: 1144px; width: 46px; height: 32px;
    background: var(--band); border-radius: 50%;
  }
  .footer-band {
    position: absolute; left: 0; top: 1158px; width: 849px; height: 4px;
    background: linear-gradient(90deg, var(--band), var(--band-light) 70%, rgba(216,216,216,0));
  }
</style>
</head>
<body>
<main class="catalogue-page">
  <div class="hero-scene" role="img" aria-label="Sepia photograph of tea pickers in a tea plantation"></div>
  <div class="sailboat-backdrop" role="img" aria-label="Faint sailing ship in the background"></div>

  <header>
    <div class="contact-block">
      <div class="logo-spot">Logo</div>
      <div class="contact-lines">Contact<br>Email<br>Phone<br>Web</div>
    </div>
    <div class="brand-mark">
      <span class="brand-dot"></span>
      <span class="brand-name">Lagoon Leaf Tea</span>
    </div>
  </header>

  <section class="product" style="top:320px">
    <div class="product-band"></div>
    <div class="band-ornament" role="img" aria-label="Floral ornament"></div>
    <h2 class="product-title">Vanilla Tea</h2>
    <div class="product-photo photo-vanilla" role="img" aria-label="Loose vanilla black tea leaves"></div>
    <p class="product-copy"><span class="drop-cap">C</span>lassic black Keemun tea and Polynesian vanilla of the highest quality. Keemun tea is known as one of the milder black teas and therefore the content of tannic acid is rather limited. Add to this a soft and exclusive vanilla and you get the perfect cup of tea.</p>
  </section>

  <section class="product" style="top:578px">
    <div class="product-band"></div>
    <div class="band-ornament" role="img" aria-label="Floral ornament"></div>
    <h2 class="product-title">Mamaki Tea</h2>
    <div class="product-photo photo-mamaki" role="img" aria-label="Bowl of dried mamaki leaves"></div>
    <p class="product-copy"><span class="drop-cap">M</span>amaki comes from the nettle family, so while it's technically not a tea, the leaves of this plant can be used to brew an all-natural herbal beverage with several supposed health benefits, from lowering blood pressure to aiding with depression. Fans of the nettle family of plants know it's common to find nettles with a wide range of benefits. Mamaki also plays a huge role in rainforest restoration efforts, making it a real super-plant.</p>
  </section>

  <section class="product" style="top:852px">
    <div class="product-band"></div>
    <div class="band-ornament" role="img" aria-label="Floral ornament"></div>
    <h2 class="product-title">Black Tea</h2>
    <div class="product-photo photo-black" role="img" aria-label="Rolled loose black tea leaves"></div>
    <p class="product-copy"><span class="drop-cap">O</span>ur Tropical Black teabags start with premium hand-picked Camellia Sinensis leaves, rolled and processed by orthodox methods into a superior black tea. The result is a quality tea with unique flavor and smooth taste that blends remarkably well with exotic tropical fruits to create our fragrant and flavorful teas. For optimal freshness, we blend and package our teas right here, in Hawaii. The tropical black tea flavors are bold and get richer and deeper the longer they steep. Delicious hot or iced.</p>
  </section>

  <div class="footer-band"></div>
  <div class="footer-ornament" role="img" aria-label="Floral ornament"></div>
</main>
</body>
</html>
```